Book Flyer

I want a flyer that we can use to promote this book to educators and to leaders....below is a sample flyer but I want something bold and creative and different from this....it can be completely different from what is attached. I want to be a WOW to increase sales. Please include pic of book and how folks can get a copy....I've given you a few pics but please be creative ....looking for a wow.

```html
<!DOCTYPE html>
<html lang="en">
<head>
<meta charset="utf-8">
<title>Decisive Excellence – Book Flyer</title>
<link href="https://fonts.googleapis.com/css2?family=Fira+Sans+Condensed:wght@600;700&family=PT+Sans:wght@400;700&family=PT+Sans+Narrow:wght@400;700&family=Mulish:ital,wght@1,400&display=swap" rel="stylesheet">
<style>
  :root{
    --red:#e3312d;
    --yellow:#f6be14;
    --orange:#e8891c;
    --blue:#1d4f9c;
    --ink:#1d1d1f;
    --mist:#e6ecee;
    --mist-line:#d7e1e4;
    --stage:#eceeef;
    --white:#ffffff;
  }
  *{margin:0;padding:0;box-sizing:border-box}
  html,body{width:1200px;height:848px;overflow:hidden;background:var(--stage)}
  .canvas{position:relative;width:1200px;height:848px}
  .page{position:absolute;top:63px;width:514px;height:729px;background:var(--white);overflow:hidden;box-shadow:0 3px 10px rgba(0,0,0,.18)}
  .page--front{left:65px}
  .page--back{left:607px}
  .page svg.shapes{position:absolute;inset:0}
  .abs{position:absolute}

  /* front */
  .title{left:252px;top:180px;font-family:"PT Sans",sans-serif;line-height:1}
  .title__main{display:block;color:var(--red);font-weight:700;font-size:43px;letter-spacing:.5px}
  .title__sub{display:block;color:var(--yellow);font-weight:400;font-size:43px;margin-top:3px;letter-spacing:1px}
  .endorsement{left:20px;width:474px;top:586px;text-align:center;font-family:"Mulish",sans-serif;font-style:italic;font-size:11.6px;line-height:17.3px;color:var(--ink)}
  .endorsement__by{left:20px;width:474px;top:684px;text-align:right;font-family:"Mulish",sans-serif;font-style:italic;font-size:12px;color:var(--ink)}

  /* back */
  .about__head{left:58px;top:22px;font-family:"Fira Sans Condensed",sans-serif;font-weight:700;font-size:14px;letter-spacing:.3px;color:var(--ink)}
  .about__text{left:32px;top:50px;width:440px;font-family:"Mulish",sans-serif;font-style:italic;font-size:11.4px;line-height:22px;color:var(--ink)}
  .strategies__head{left:39px;top:213px;font-family:"Fira Sans Condensed",sans-serif;font-weight:700;font-size:16.5px;line-height:21px;letter-spacing:1px;color:var(--red)}
  .pillar{left:32px;width:190px}
  .pillar__name{font-family:"Fira Sans Condensed",sans-serif;font-weight:700;font-size:17px;letter-spacing:.4px;line-height:20px;margin-left:1px}
  .pillar__quote{font-family:"PT Sans Narrow",sans-serif;font-size:14.3px;line-height:17.7px;color:var(--ink);margin-top:6px}
  .pillar__by{font-family:"PT Sans Narrow",sans-serif;font-size:12px;text-align:right;color:var(--ink);margin-top:3px}
  .pillar--equity{top:298px}
  .pillar--equity .pillar__name{color:var(--blue)}
  .pillar--change{top:407px;width:178px}
  .pillar--change .pillar__name{color:var(--red)}
  .pillar--comm{top:523px}
  .pillar--comm .pillar__name{color:var(--orange)}
  .contact{left:32px;top:679px;font-family:"Fira Sans Condensed",sans-serif;font-weight:600;font-size:15px;color:var(--white);letter-spacing:.2px}
</style>
</head>
<body>
<div class="canvas">

  <!-- FRONT PAGE -->
  <section class="page page--front">
    <svg class="shapes" viewBox="0 0 514 729" width="514" height="729" aria-hidden="false">
      <defs>
        <linearGradient id="bookFill" x1="0" y1="0" x2="0" y2="1">
          <stop offset="0" stop-color="#1d2d5a"/>
          <stop offset=".45" stop-color="#2f5ea8"/>
          <stop offset=".46" stop-color="#e3312d"/>
          <stop offset=".72" stop-color="#e3312d"/>
          <stop offset=".73" stop-color="#ffffff"/>
          <stop offset="1" stop-color="#f2f2f2"/>
        </linearGradient>
        <linearGradient id="bookReflect" x1="0" y1="0" x2="0" y2="1">
          <stop offset="0" stop-color="#e3312d" stop-opacity=".18"/>
          <stop offset="1" stop-color="#ffffff" stop-opacity="0"/>
        </linearGradient>
        <linearGradient id="portraitFill" x1="0" y1="0" x2="0" y2="1">
          <stop offset="0" stop-color="#111"/>
          <stop offset=".55" stop-color="#3a2a22"/>
          <stop offset="1" stop-color="#dfe3ea"/>
        </linearGradient>
      </defs>
      <!-- soft mist shapes -->
      <circle cx="155" cy="760" r="300" fill="var(--mist)"/>
      <circle cx="500" cy="68" r="141" fill="var(--mist)"/>
      <circle cx="500" cy="68" r="150" fill="none" stroke="var(--mist-line)" stroke-width="1.5"/>
      <!-- big red ring -->
      <circle cx="110" cy="227" r="201" fill="none" stroke="var(--red)" stroke-width="90"/>
      <circle cx="110" cy="227" r="256" fill="none" stroke="var(--red)" stroke-width="2"/>
      <!-- title knock-out -->
      <rect x="251" y="167" width="263" height="113" fill="var(--white)"/>
      <!-- book -->
      <rect x="44" y="44" width="171" height="259" fill="url(#bookFill)" role="img" aria-label="Book cover of Decisive Excellence by S. Marcus Reed" transform="rotate(-2 130 170)"/>
      <rect x="44" y="306" width="171" height="90" fill="url(#bookReflect)"/>
      <!-- author portrait -->
      <circle cx="288" cy="439" r="124" fill="none" stroke="#ecc4b5" stroke-width="1"/>
      <circle cx="280" cy="449" r="116" fill="none" stroke="#ecc4b5" stroke-width="1"/>
      <circle cx="288" cy="439" r="103" fill="var(--red)"/>
      <circle cx="288" cy="439" r="89" fill="var(--white)"/>
      <circle cx="288" cy="439" r="83" fill="url(#portraitFill)" role="img" aria-label="Portrait of author S. Marcus Reed in shirt and tie, arms crossed"/>
    </svg>

    <h1 class="abs title">
      <span class="title__main">DECISIVE</span>
      <span class="title__sub">EXCELLENCE</span>
    </h1>

    <p class="abs endorsement">“Decisive Excellence is a book written for all leaders. Dr.Marcus Reed speaks from real life experiences that are relatable and from the heart. His leadership steps have helped him develop into one of the most accomplished administrative leaders in the country. The three specific strategies outlined in this book will transform ypor leadership skills and help you stay on track to ensure success.”</p>
    <p class="abs endorsement__by">- Laura Whitfield, Principal</p>
  </section>

  <!-- BACK PAGE -->
  <section class="page page--back">
    <svg class="shapes" viewBox="0 0 514 729" width="514" height="729">
      <defs>
        <linearGradient id="photoFill" x1="0" y1="0" x2="1" y2="1">
          <stop offset="0" stop-color="#9fb7d4"/>
          <stop offset=".45" stop-color="#6b7c8c"/>
          <stop offset=".75" stop-color="#28303c"/>
          <stop offset="1" stop-color="#1a1e26"/>
        </linearGradient>
      </defs>
      <circle cx="47" cy="0" r="112" fill="var(--mist)"/>
      <circle cx="47" cy="0" r="120" fill="none" stroke="var(--mist-line)" stroke-width="1.5"/>
      <!-- partial red ring -->
      <circle cx="26" cy="235" r="57" fill="none" stroke="var(--red)" stroke-width="23"/>
      <circle cx="30" cy="238" r="79" fill="none" stroke="#ecc4b5" stroke-width="1"/>
      <rect x="36" y="207" width="160" height="60" fill="var(--white)"/>
      <!-- photo area -->
      <circle cx="810" cy="617" r="625" fill="none" stroke="var(--mist-line)" stroke-width="2"/>
      <circle cx="804" cy="617" r="607" fill="none" stroke="var(--white)" stroke-width="4"/>
      <circle cx="804" cy="617" r="596" fill="url(#photoFill)" role="img" aria-label="Photo of the author in a suit reading the book on a city street"/>
      <!-- contact band -->
      <polygon points="0,671 232,671 255,708 0,708" fill="var(--red)"/>
    </svg>

    <h2 class="abs about__head">ABOUT DR. REED</h2>
    <p class="abs about__text">Distinguished as a vibrant, visionary, and innovative leader who recognizes that humility is the most important trait a leader can possess. Dr.Reed uses his prior experiences in business, education and nonprofit to assist organization leaders from all industries build internal leadership capacity. Including strategy &amp; talent management <br>and development to maximize organizational potential and <br>success.</p>

    <h2 class="abs strategies__head">3 FUNDAMENT STRATEGIES<br>THAT DRIVE LEADERSHIP</h2>

    <div class="abs pillar pillar--equity">
      <h3 class="pillar__name">EQUITY</h3>
      <p class="pillar__quote">“Fariness does not mean everyone gets the same. Fairness means everyone gets what they need.”</p>
      <p class="pillar__by">Nora Ellison</p>
    </div>
    <div class="abs pillar pillar--change">
      <h3 class="pillar__name">CHANGE</h3>
      <p class="pillar__quote">“If you di not change direction, you may end up where you are heading.”</p>
      <p class="pillar__by">Chen Wei</p>
    </div>
    <div class="abs pillar pillar--comm">
      <h3 class="pillar__name">COMMUNICATION</h3>
      <p class="pillar__quote">“The single biggest problem in communication is the illusion that is has taken place.”</p>
      <p class="pillar__by">Edmund Hale</p>
    </div>

    <p class="abs contact">info@thereedgroup.com</p>
  </section>

</div>
</body>
</html>
```